Flyer für Trainingszentrum
Zielgruppe
Das Vitaforma ist eine, an eine Arztpraxis angeschlossene, Trainingseinrichtung. Hier können Personen nach Verletzungen gezielt und betreut ihre Leistungsfähigkeit zurück erlangen. Ebenso können Personen mit z.B. chronischen Rückenschmerzen oder anderen Beschwerden (Knie, Ellenbogen, Schulter-/Nackenschmerz) unter fachlicher Betreuung durch einen Sportwissenschaftler und Sportmediziner ihre Schmerzen weg trainieren. Aber auch Personen, die einfach ein Gesundheitsförderndes Training unter exklusiver Betreuung suchen, sind bei uns bestens aufgehoben.
Aufgabenstellung
Der Flyer soll im A5 Format und zweiseitig sein (oder auch Faltblatt-Ideen sind willkommen).
Der Flyer soll mit der Tagespost beim potenziellen Kunden landen. Er soll auf der Front Aufmerksamkeit erwecken und nicht überladen sein.
Botschaft: Exklusive Betreuung – Mehr als ein gewöhnliches Fitness-Studio
Auf der Rückseite sollte eine kurze Beschreibung und der Kontakt zu finden sein.
Adresse
Telefon
E-Mail Adresse
Aktuelles auf der Homepage: www.vitaforma-beispiel.ch
oder auf Facebook: Vitaforma.Zentrum
Die farbliche Gestaltung sollte unserem Logo entsprechen (siehe Anhang)

```html
<!DOCTYPE html>
<html lang="de">
<head>
<meta charset="utf-8">
<title>Vitaforma Talmatt – Flyer</title>
<link href="https://fonts.googleapis.com/css2?family=Lobster&family=Lato:wght@400;700&display=swap" rel="stylesheet">
<style>
  :root {
    --stage: #2e2e2e;
    --paper: #f4f5f6;
    --paper-shade: #e3e5e8;
    --brand-blue: #1b5fae;
    --band-dark: #0c4f9e;
    --band-light: #3aa6e3;
    --band-halo: #a9d6f3;
    --green-dark: #5e9e1e;
    --green-light: #b9d84a;
    --yellow: #e3d81a;
    --yellow-soft: #f1ec8c;
    --white: #ffffff;
  }
  * { margin: 0; padding: 0; box-sizing: border-box; }
  html, body {
    width: 1048px;
    height: 1200px;
    overflow: hidden;
    background: var(--stage);
  }
  .flyer {
    position: absolute;
    left: 251px;
    top: 20px;
    width: 545px;
    height: 1160px;
    overflow: hidden;
    box-shadow: 0 12px 40px rgba(0,0,0,.45);
  }
  .flyer svg { display: block; width: 100%; height: 100%; }
  .brand-name {
    font-family: "Lobster", cursive;
    font-size: 27px;
    fill: var(--brand-blue);
  }
  .brand-sub {
    font-family: "Lato", sans-serif;
    font-size: 17px;
    fill: var(--brand-blue);
    letter-spacing: .5px;
  }
  .tagline {
    font-family: "Lobster", cursive;
    font-size: 28px;
    fill: var(--white);
  }
</style>
</head>
<body>
  <div class="flyer">
    <svg viewBox="0 0 545 1160" xmlns="http://www.w3.org/2000/svg">
      <defs>
        <linearGradient id="paperFill" x1="0" y1="0" x2="0" y2="1">
          <stop offset="0" stop-color="var(--paper-shade)"/>
          <stop offset=".45" stop-color="var(--paper)"/>
          <stop offset="1" stop-color="var(--paper-shade)"/>
        </linearGradient>
        <linearGradient id="bandFill" x1="0" y1="1" x2="1" y2="0">
          <stop offset="0" stop-color="var(--band-light)"/>
          <stop offset=".5" stop-color="var(--band-dark)"/>
          <stop offset="1" stop-color="#1e7fd0"/>
        </linearGradient>
        <linearGradient id="classPhoto" x1="0" y1="0" x2="1" y2="1">
          <stop offset="0" stop-color="#b9d6e6"/>
          <stop offset=".5" stop-color="#8fd3d6"/>
          <stop offset="1" stop-color="#d9b7a2"/>
        </linearGradient>
        <linearGradient id="groupPhoto" x1="0" y1="0" x2="1" y2="1">
          <stop offset="0" stop-color="#9fdbe8"/>
          <stop offset=".45" stop-color="#d8b49d"/>
          <stop offset=".75" stop-color="#ef8fbd"/>
          <stop offset="1" stop-color="#8fd6cf"/>
        </linearGradient>
      </defs>

      <rect class="paper" width="545" height="1160" fill="url(#paperFill)"/>

      <g class="swoosh-yellow" fill="none">
        <path d="M200 300 C300 190 450 220 560 290" stroke="var(--yellow-soft)" stroke-width="30"/>
        <path d="M220 330 C320 240 460 300 560 350" stroke="var(--yellow)" stroke-width="14"/>
        <path d="M230 260 C330 150 470 160 560 190" stroke="var(--yellow-soft)" stroke-width="10" opacity=".7"/>
        <path d="M260 300 C380 230 470 280 560 360" stroke="var(--yellow-soft)" stroke-width="8" opacity=".8"/>
      </g>

      <g class="swoosh-green" fill="none">
        <path d="M-20 120 C70 110 110 280 170 430 C210 530 260 590 360 620" stroke="var(--green-light)" stroke-width="46"/>
        <path d="M-10 115 C85 125 120 290 180 445 C220 540 270 595 360 612" stroke="var(--green-dark)" stroke-width="14"/>
        <path d="M40 -10 C110 60 150 230 210 390 C240 470 290 540 360 580" stroke="var(--green-light)" stroke-width="12" opacity=".8"/>
        <path d="M-20 250 C40 310 70 430 120 540 C160 610 250 650 340 660" stroke="var(--green-light)" stroke-width="8" opacity=".6"/>
      </g>

      <g role="img" aria-label="Foto: Frauen beim Gymnastik-Kurs im Schneidersitz mit Bällen">
        <path d="M130 350 C130 260 200 220 275 220 C360 220 415 270 412 350 C410 430 350 480 275 480 C195 480 130 440 130 350 Z" fill="url(#classPhoto)" stroke="var(--white)" stroke-width="6"/>
      </g>

      <g role="img" aria-label="Foto: lachende Gruppe junger Leute im Fitnessstudio mit Hanteln">
        <path d="M-10 960 C200 900 420 760 560 620 L560 1170 L-10 1170 Z" fill="url(#groupPhoto)"/>
      </g>
      <path d="M-10 950 C200 890 420 750 560 610" fill="none" stroke="var(--white)" stroke-width="20"/>

      <g class="tagline-band" fill="none">
        <path d="M-10 790 C200 740 440 620 485 445 C505 360 525 310 570 285" stroke="var(--band-halo)" stroke-width="100" opacity=".55"/>
        <path id="bandLine" d="M-10 770 C200 720 430 600 470 430 C490 345 515 300 570 275" stroke="url(#bandFill)" stroke-width="70"/>
        <path d="M-10 738 C190 690 405 578 440 420 C460 335 490 280 570 245" stroke="var(--white)" stroke-width="3" opacity=".6"/>
      </g>

      <path id="taglinePath" d="M-10 770 C200 720 430 600 470 430" fill="none"/>
      <text class="tagline" dominant-baseline="middle">
        <textPath href="#taglinePath" startOffset="40">Mehr als ein gewöhnliches Fitness-Studio</textPath>
      </text>

      <g class="brand">
        <circle cx="300" cy="98" r="9" fill="var(--brand-blue)"/>
        <text class="brand-name" x="318" y="108">Vitaforma Talmatt</text>
        <text class="brand-sub" x="320" y="134">Trainingscenter</text>
      </g>
    </svg>
  </div>
</body>
</html>
```